Landing Page - Lending & Lantern

Need a singular landing page that will eventually link to podcast and direct people to my page. I need it to work with TallyMorrow.

The page is geared about small business owners and linking them with high quality banker to obtain financing. It should be professional, connect to bourbon as an underlying tone. It's all about qualify and integrity.

It needs to be put in Wordpress.
I don't know the difference between coded and uncoded, I just want it done.

Target Market(s)

Business Owners and those needing help with financing. The people we're trying to help aren't rich, they are successful but need help.

Industry/Entity Type

Finance & Bourbon

Coding

Coded - Design and coding required

Number of Pages Required

1 page

Colors
0054AA
0677BA
7BADD7
CADEEF
E8F1F8
0094D4
00A9DD
6FCCEA
C7EBF8
E9F6FB

Requirements
Must have
• Link to send email
Nice to have
• Use colors and fonts in branding.

```html
<!DOCTYPE html>
<html lang="en">
<head>
<meta charset="utf-8">
<title>Lending &amp; Lantern</title>
<link rel="stylesheet" href="https://fonts.googleapis.com/css2?family=Archivo:wdth,wght@125,800;125,900&family=Poppins:wght@400;500;600;700&display=swap">
<style>
:root{
  --brand:#0677BA;
  --brand-deep:#0054AA;
  --brand-soft:#CADEEF;
  --brand-pale:#E8F1F8;
  --sky:#00A9DD;
  --sky-light:#6FCCEA;
  --sky-pale:#C7EBF8;
  --hero-a:#7BADD7;
  --hero-b:#CADEEF;
  --ink:#111111;
  --body:#555b60;
  --white:#ffffff;
  --star:#f5b50a;
  --line:#e3e8ea;
}
*{box-sizing:border-box;margin:0;padding:0}
html,body{width:1200px;height:3116px;overflow:hidden}
body{position:relative;background:var(--white);font-family:"Poppins",sans-serif;color:var(--ink)}
a{text-decoration:none;color:inherit}
.abs{position:absolute}
.display{font-family:"Archivo",sans-serif;font-stretch:125%;font-weight:900;text-transform:uppercase;letter-spacing:-.5px}

/* hero */
.hero{left:0;top:0;width:1200px;height:633px;border-radius:0 0 100px 100px;overflow:hidden;
  background:linear-gradient(100deg,var(--hero-a) 0%,#9cc3e3 55%,var(--hero-b) 100%)}
.hero-photo{left:640px;top:0;width:560px;height:633px;
  background:radial-gradient(ellipse 210px 230px at 220px 400px,#f6f9fc 0%,#e0ebf5 55%,rgba(202,222,239,0) 100%)}
.socials{left:114px;top:38px;display:flex;gap:13px}
.socials span{width:26px;height:26px;border-radius:50%;background:var(--brand)}
.brand{font-family:"Poppins",sans-serif;font-weight:700;color:var(--white);font-size:19px;letter-spacing:.5px}
.hero .brand{left:500px;top:40px;width:200px;text-align:center}
.nav{left:762px;top:42px;display:flex;gap:29px;font-size:11px;color:var(--white)}
.hero h1{left:111px;top:178px;font-size:58px;line-height:61px;color:var(--white)}
.hero p{left:111px;top:368px;width:430px;font-size:13.5px;line-height:20px;color:#f4f9fd}
.btn{display:flex;align-items:center;justify-content:center;border-radius:30px;font-size:12.5px;font-weight:600;text-transform:uppercase;letter-spacing:.3px}
.btn-white{left:112px;top:425px;width:188px;height:37px;background:var(--white);color:var(--brand)}
.btn-brand{left:312px;top:425px;width:161px;height:37px;background:var(--brand);color:var(--white)}

/* access */
.access h2{left:111px;top:688px;font-size:31px;line-height:38px}
.access .lead{left:111px;top:768px;font-size:12.5px;font-weight:600}
.features{left:111px;top:798px;list-style:none}
.features li{display:flex;align-items:center;gap:12px;height:31.5px;font-size:10.5px;color:var(--body)}
.features svg{width:19px;height:19px;stroke:var(--brand);fill:none;stroke-width:1.6}
.btn-app{left:113px;top:932px;width:192px;height:36px;background:var(--brand);color:var(--white)}
.dash-back{left:686px;top:688px;width:402px;height:230px;background:linear-gradient(180deg,#f4f6fb,#e9edf5);border-radius:6px;box-shadow:0 8px 24px rgba(40,60,90,.15)}
.dash-front{left:609px;top:777px;width:307px;height:190px;background:linear-gradient(90deg,#6f8cb6 0 19%,#f3f5fa 19% 100%);border-radius:6px;box-shadow:0 10px 28px rgba(40,60,90,.22)}

/* offer */
.offer-band{left:0;top:1030px;width:1200px;height:426px;background:var(--brand-pale)}
.section-title{width:1200px;left:0;text-align:center;font-size:31px}
.offer-title{top:1086px}
.offer-card{top:1142px;width:310px;height:253px;background:var(--white);border-radius:6px;box-shadow:0 4px 16px rgba(0,0,0,.05);padding:32px 25px 0}
.offer-card.active{background:var(--brand);color:var(--white)}
.offer-icon{width:60px;height:60px;border-radius:50%;background:var(--brand-soft);display:flex;align-items:center;justify-content:center;margin-bottom:12px}
.active .offer-icon{background:rgba(255,255,255,.18)}
.offer-icon svg{width:44px;height:44px;stroke:var(--brand);fill:none;stroke-width:2}
.active .offer-icon svg{stroke:var(--white)}
.offer-card h3{font-size:14px;font-weight:600;line-height:20px;height:46px}
.offer-card p{font-size:10.5px;line-height:16px;color:var(--body);height:52px}
.active p{color:#e6f0f9}
.offer-card a{font-size:12.5px;font-weight:600;color:var(--brand);border-bottom:1px solid currentColor}
.active a{color:var(--white)}

/* testimonials */
.testi-band{left:0;top:1456px;width:1200px;height:577px;background:var(--brand);border-radius:120px 0 0 0}
.testi-title{top:1506px;color:var(--white)}
.testi-card{top:1606px;width:306px;height:360px;background:var(--white);border-radius:6px;padding:0 24px}
.avatar{position:absolute;left:22px;top:-34px;width:102px;height:102px;border-radius:50%;border:4px solid var(--brand);background:linear-gradient(160deg,#e3e6e8,#9aa3aa)}
.quote{position:absolute;right:22px;top:6px;font-family:"Archivo",sans-serif;font-weight:900;font-size:110px;line-height:110px;color:var(--sky-pale)}
.testi-card h4{margin-top:96px;font-size:15.5px;font-weight:600}
.testi-card .role{font-size:12.5px;color:var(--body);padding-bottom:14px;border-bottom:1px solid var(--line);margin-right:14px}
.testi-card .text{margin-top:16px;font-size:11.5px;line-height:19px;color:var(--body)}
.testi-card .qs{margin-top:12px;font-size:11px;font-weight:600}
.stars{margin-top:4px;color:var(--star);font-size:17px;letter-spacing:8px}
.circle-btn{width:60px;height:60px;border-radius:50%;display:flex;align-items:center;justify-content:center}
.circle-btn svg{width:30px;height:16px;fill:none;stroke-width:1.6}
.arrow-l-w{left:44px;top:1756px;border:1.5px solid var(--white)}
.arrow-l-w svg{stroke:var(--white)}
.arrow-r-w{left:1096px;top:1756px;background:var(--white)}
.arrow-r-w svg{stroke:var(--brand)}

/* guidance */
.guide h2{left:111px;top:2088px;font-size:31px;line-height:38px}
.arrow-l-t{left:953px;top:2101px;border:1.5px solid var(--brand)}
.arrow-l-t svg{stroke:var(--brand)}
.arrow-r-t{left:1026px;top:2101px;background:var(--brand)}
.arrow-r-t svg{stroke:var(--white)}
.guide-card{top:2186px;width:345px;height:379px;background:var(--white);box-shadow:0 4px 18px rgba(0,0,0,.07)}
.guide-photo{width:100%;height:210px}
.guide-body{padding:24px 25px 0}
.guide-body h3{font-size:11.5px;font-weight:700;text-transform:uppercase}
.guide-body p{margin-top:10px;font-size:11px;line-height:16px;color:var(--body);height:46px}
.btn-outline{display:inline-flex;align-items:center;height:37px;padding:0 25px;border:1.5px solid var(--brand);border-radius:30px;color:var(--brand);font-size:11.5px;font-weight:600;text-transform:uppercase;letter-spacing:.4px}

/* help */
.help{left:0;top:2565px;width:1200px;height:351px;background:var(--white);border-radius:0 0 120px 0;z-index:2}
.help h2{top:75px}
.help-item{position:absolute;top:127px;width:170px;text-align:center}
.help-circle{width:120px;height:120px;margin:0 auto;border-radius:50%;background:var(--white);box-shadow:0 4px 16px rgba(0,0,0,.08);display:flex;align-items:center;justify-content:center}
.help-circle svg{width:50px;height:50px;fill:none;stroke:var(--brand);stroke-width:2.2;stroke-linecap:round;stroke-linejoin:round}
.help-item span{display:block;margin-top:24px;font-size:13px;color:#444}

/* footer */
.footer{left:0;top:2760px;width:1200px;height:356px;background:var(--brand-deep)}
.footer-brand{left:140px;top:2980px;z-index:3}
.on-footer{z-index:3;color:var(--white)}
.copyright{left:111px;top:3058px;font-size:10.5px}
.fcol{list-style:none;font-size:12px;line-height:22px}
.fhead{font-size:12.5px;font-weight:600}
.subscribe{left:759px;top:2979px;width:328px;height:50px;border:1px solid var(--white);border-radius:30px;display:flex;align-items:center;justify-content:space-between;padding:0 4px 0 14px;font-size:11px}
.subscribe b{height:38px;width:122px;background:var(--white);color:var(--brand-deep);border-radius:30px;display:flex;align-items:center;justify-content:center;font-size:12px;font-weight:600}
.fsocial{left:759px;top:3058px;display:flex;gap:9px}
.fsocial span{width:18px;height:18px;border-radius:50%;background:var(--sky)}
</style>
</head>
<body>

<header class="abs hero">
  <div class="abs hero-photo" role="img" aria-label="White piggy bank with coins dropping into its slot"></div>
  <div class="abs socials"><span></span><span></span><span></span><span></span></div>
  <div class="abs brand">Lending &amp; Lantern</div>
  <nav class="abs nav"><a href="#access">Access Us</a><a href="#offer">Services</a><a href="#guide">Why Choose Us</a><a href="#voices">Testimonials</a></nav>
  <h1 class="abs display">Financing in<br>the palm<br>of your hand</h1>
  <p class="abs">Small business owners: get matched with a trusted banker and the financing your business has earned.</p>
  <a class="abs btn btn-white" href="mailto:hello@lendingandlantern.example">Email a banker</a>
  <a class="abs btn btn-brand" href="#podcast">Hear the podcast</a>
</header>

<section class="access" id="access">
  <h2 class="abs display">Access Lending &amp; Lantern<br>wherever you go.</h2>
  <div class="abs lead">Manage business funds from anywhere with the Harbor Ledger App.</div>
  <ul class="abs features">
    <li><svg viewBox="0 0 20 20"><path d="M3 7h13l-3-3M17 13H4l3 3"/></svg>Transfer money between your accounts.</li>
    <li><svg viewBox="0 0 20 20"><rect x="2" y="4" width="16" height="12" rx="1.5"/><circle cx="6" cy="13" r="1.8"/><path d="M10 8h5"/></svg>Deposit checks.</li>
    <li><svg viewBox="0 0 20 20"><rect x="3" y="2" width="14" height="16" rx="1.5"/><path d="M10 5v6M8 7h4M6 14h8"/></svg>Manage and pay bills.</li>
    <li><svg viewBox="0 0 20 20"><path d="M4 4h-1v12h14V4h-1"/><path d="M12 6.5c-.5-.8-3.5-1-3.5.8s3.5 1 3.5 3-3 1.6-3.6.7M10 4.5v10"/></svg>Send, receive and request money.</li>
  </ul>
  <a class="abs btn btn-app">Download the app</a>
  <div class="abs dash-back" role="img" aria-label="Banking dashboard screen with balance chart and progress rings"></div>
  <div class="abs dash-front" role="img" aria-label="Banking dashboard screen with earnings, line chart and bar chart"></div>
</section>

<div class="abs offer-band" id="offer"></div>
<h2 class="abs display section-title offer-title">What we offer</h2>
<article class="abs offer-card" style="left:111px">
  <div class="offer-icon"><svg viewBox="0 0 44 44"><rect x="4" y="10" width="36" height="26" rx="3"/><path d="M4 18h36M10 28h8"/></svg></div>
  <h3>Enjoy 0% intro APR for 21 months</h3>
  <p>on business credit lines from account opening, for purchases and balance transfers. Terms apply.</p>
  <a href="mailto:hello@lendingandlantern.example">Learn More</a>
</article>
<article class="abs offer-card active" style="left:444px">
  <div class="offer-icon"><svg viewBox="0 0 44 44"><circle cx="26" cy="12" r="6"/><ellipse cx="20" cy="28" rx="14" ry="9"/><path d="M12 36v4M28 36v4"/></svg></div>
  <h3>4.00% 3 month interest rate with 1.19% APY</h3>
  <p>With $25,000 new money and minimum balance. Open Business Savings by 9/26/2023.</p>
  <a href="mailto:hello@lendingandlantern.example">Learn More</a>
</article>
<article class="abs offer-card" style="left:778px">
  <div class="offer-icon"><svg viewBox="0 0 44 44"><rect x="4" y="10" width="34" height="24" rx="3"/><circle cx="12" cy="18" r="2.5"/><path d="M32 18c2 2 2 6 0 8M36 16c3 3 3 9 0 12"/></svg></div>
  <h3>Earn Points on Rent</h3>
  <p>Redeem your shop rent for travel, credit and more</p>
  <a href="mailto:hello@lendingandlantern.example">Learn More</a>
</article>

<div class="abs testi-band" id="voices"></div>
<h2 class="abs display section-title testi-title">What customer say us</h2>
<a class="abs circle-btn arrow-l-w"><svg viewBox="0 0 30 16"><path d="M29 8H2M8 2 2 8l6 6"/></svg></a>
<a class="abs circle-btn arrow-r-w"><svg viewBox="0 0 30 16"><path d="M1 8h27M22 2l6 6-6 6"/></svg></a>
<article class="abs testi-card" style="left:117px">
  <div class="avatar" role="img" aria-label="Portrait photo of the customer"></div><div class="quote">”</div>
  <h4>Dorian K. Maddox</h4><div class="role">Business Consultant</div>
  <p class="text">Lorem ipsum dolor sit amet, consectetur adipiscing elit, sed do eiusmod tempor incididunt ut labore et dolore magna aliqua. Quis ipsum suspendisse ultrices gravida. Risus commodo viverra maecenas accumsan lacus vel facilisis.</p>
  <div class="qs">Quality Services</div><div class="stars">★★★★★</div>
</article>
<article class="abs testi-card" style="left:447px">
  <div class="avatar" role="img" aria-label="Portrait photo of the customer"></div><div class="quote">”</div>
  <h4>Ellis R. Carrow</h4><div class="role">Senior Manager</div>
  <p class="text">Lorem ipsum dolor sit amet, consectetur adipiscing elit, sed do eiusmod tempor incididunt ut labore et dolore magna aliqua. Quis ipsum suspendisse ultrices gravida. Risus commodo viverra maecenas accumsan lacus vel facilisis.</p>
  <div class="qs">Quality Services</div><div class="stars">★★★★★</div>
</article>
<article class="abs testi-card" style="left:777px">
  <div class="avatar" role="img" aria-label="Portrait photo of the customer"></div><div class="quote">”</div>
  <h4>Nadia P. Holloway</h4><div class="role">Marketing Officer</div>
  <p class="text">Lorem ipsum dolor sit amet, consectetur adipiscing elit, sed do eiusmod tempor incididunt ut labore et dolore magna aliqua. Quis ipsum suspendisse ultrices gravida. Risus commodo viverra maecenas accumsan lacus vel facilisis.</p>
  <div class="qs">Quality Services</div><div class="stars">★★★★★</div>
</article>

<section class="guide" id="guide">
  <h2 class="abs display">Financial guidance<br>and support</h2>
  <a class="abs circle-btn arrow-l-t"><svg viewBox="0 0 30 16"><path d="M29 8H2M8 2 2 8l6 6"/></svg></a>
  <a class="abs circle-btn arrow-r-t"><svg viewBox="0 0 30 16"><path d="M1 8h27M22 2l6 6-6 6"/></svg></a>
  <article class="abs guide-card" style="left:111px">
    <div class="guide-photo" role="img" aria-label="Hands presenting stacked coins over a pie chart on a desk" style="background:linear-gradient(160deg,#e9ebec,#b9c1c4 60%,#9cc3e3)"></div>
    <div class="guide-body"><h3>Get tools. Get tips. Get peace of mind.</h3><p>Discover digital tools to help your business budget, save, manage credit, and more</p><a class="btn-outline">Access the toolkit</a></div>
  </article>
  <article class="abs guide-card" style="left:484px">
    <div class="guide-photo" role="img" aria-label="Piggy bank beside stacks of coins with a coffee cup" style="background:linear-gradient(160deg,#cfd3d4,#eef0f0 55%,#c9a85a)"></div>
    <div class="guide-body"><h3>Spend less. Save more. Relax more.</h3><p>These four steps could help your business make it happen</p><a class="btn-outline">Manage spending and saving</a></div>
  </article>
  <article class="abs guide-card" style="left:855px">
    <div class="guide-photo" role="img" aria-label="Person writing with a pen over financial charts and a laptop" style="background:linear-gradient(160deg,#5a6670,#d9dcdf 55%,#7BADD7)"></div>
    <div class="guide-body"><h3>Save. Invest. Retire well.</h3><p>Discover how to start saving to meet your retirement goals</p><a class="btn-outline">Get ready for retirement</a></div>
  </article>
</section>

<div class="abs footer"></div>
<section class="abs help">
  <h2 class="abs display section-title">How can we help?</h2>
  <div class="help-item" style="left:302px"><div class="help-circle"><svg viewBox="0 0 50 50"><path d="M25 38s-12-12-12-21a12 12 0 0 1 24 0c0 9-12 21-12 21z"/><circle cx="25" cy="17" r="4.5"/><path d="M16 36c-6 1-8 3-8 5 0 3 8 5 17 5s17-2 17-5c0-2-2-4-8-5"/></svg></div><span>Find a location ⌄</span></div>
  <a class="help-item" style="left:515px" href="mailto:hello@lendingandlantern.example"><div class="help-circle"><svg viewBox="0 0 50 50"><rect x="6" y="9" width="38" height="34" rx="2"/><path d="M6 18h38M15 5v8M35 5v8M18 30l5 5 10-10"/></svg></div><span>Make an appointment ⌄</span></a>
  <div class="help-item" style="left:727px"><div class="help-circle"><svg viewBox="0 0 50 50"><path d="M17 16a8 8 0 1 1 12 7c-3 2-4 3.5-4 7v3"/><rect x="21" y="38" width="8" height="7"/></svg></div><span>Quick help ⌄</span></div>
</section>

<div class="abs brand footer-brand">Lending &amp; Lantern</div>
<div class="abs copyright on-footer">Copyright © 2010-2023 All rights reserved.</div>
<ul class="abs fcol on-footer" style="left:376px;top:2947px"><li>Support</li><li>Online advertising</li><li>Cobrowse</li><li>Security</li><li>Privacy</li></ul>
<ul class="abs fcol on-footer" style="left:569px;top:2948px"><li>Access Us</li><li id="podcast">Services</li><li>Why Choose Us</li><li>Testimonials</li></ul>
<div class="abs fhead on-footer" style="left:759px;top:2949px">Get Connect</div>
<a class="abs subscribe on-footer" href="mailto:hello@lendingandlantern.example">Enter Email<b>SUBSCRIBE</b></a>
<div class="abs fhead on-footer" style="left:759px;top:3037px">Follow us</div>
<div class="abs fsocial on-footer"><span></span><span></span><span></span><span></span></div>

</body>
</html>
```